Need new label for my eczema cream. Pinegrove Soothe. PLS NOTHING LAME AND CLIP ART-ISH!

Think corvanta website meets eczema....our site is pinegrovesoothe.com ill attach our current logo.

```html
<!DOCTYPE html>
<html lang="en">
<head>
<meta charset="utf-8">
<title>Pinegrove Soothe – Soothing Cream Label</title>
<link rel="stylesheet" href="https://fonts.googleapis.com/css2?family=Jost:wght@300;400;600&display=swap">
<style>
  :root {
    --backdrop: #f7f7f7;
    --label: #d8d6d3;
    --ink-navy: #0f3f5c;
    --ink-green: #3d9a55;
    --wave-deep: #0e3550;
    --wave-teal: #2aa3b3;
    --wave-foam: #bfe2e5;
  }
  html, body {
    margin: 0;
    padding: 0;
    width: 1200px;
    height: 753px;
    overflow: hidden;
    background: var(--backdrop);
  }
  .canvas {
    position: relative;
    width: 1200px;
    height: 753px;
  }
  .label {
    position: absolute;
    left: 250px;
    top: 90px;
    width: 700px;
    height: 574px;
    background: var(--label);
    color: var(--ink-navy);
    overflow: hidden;
  }
  .label__category {
    position: absolute;
    left: 49px;
    top: 80px;
    margin: 0;
    font-family: "Jost", sans-serif;
    font-weight: 400;
    font-size: 25px;
    letter-spacing: 0.42em;
  }
  .label__brand {
    position: absolute;
    left: 49px;
    top: 134px;
    margin: 0;
    font-family: "Jost", sans-serif;
    font-weight: 600;
    font-size: 80px;
    line-height: 1;
    letter-spacing: 0.01em;
    text-transform: uppercase;
    color: var(--ink-navy);
  }
  .label__ingredients {
    position: absolute;
    left: 49px;
    right: 49px;
    top: 322px;
    margin: 0;
    padding: 0;
    list-style: none;
    display: flex;
    justify-content: space-between;
    align-items: center;
    font-family: "Jost", sans-serif;
    font-weight: 300;
    font-size: 31px;
    color: var(--ink-green);
  }
  .label__dot {
    width: 10px;
    height: 10px;
    border-radius: 50%;
    background: var(--ink-navy);
  }
  .label__volume {
    position: absolute;
    left: 49px;
    top: 398px;
    margin: 0;
    font-family: "Jost", sans-serif;
    font-weight: 600;
    font-size: 17px;
  }
  .label__waves {
    position: absolute;
    left: 0;
    right: 0;
    bottom: 0;
    height: 122px;
    background: linear-gradient(180deg, var(--wave-deep) 0%, var(--wave-teal) 35%, var(--wave-foam) 55%, var(--wave-teal) 75%, var(--wave-deep) 100%);
  }
</style>
</head>
<body>
<main class="canvas">
  <section class="label">
    <p class="label__category">SOOTHING CREAM</p>
    <h1 class="label__brand">Pinegrove<br>Soothe</h1>
    <ul class="label__ingredients">
      <li>Sea Moss</li>
      <li class="label__dot" aria-hidden="true"></li>
      <li>Aloe Vera</li>
      <li class="label__dot" aria-hidden="true"></li>
      <li>Oats</li>
    </ul>
    <p class="label__volume">4 fl oz / 118 mL</p>
    <div class="label__waves" role="img" aria-label="Band of stylised navy and teal ocean waves"></div>
  </section>
</main>
</body>
</html>
```